Home page web design for a lawn specialist business

-The design must be based around the attached HPID (home page information design) called Turf Tidings HPID. I've attached Word and PDF versions - these are the same. The table boxes are just for approximate placement of information and you can use boxes and bold shapes for this design.

All fonts used in the HPID are only examples - you can use any Google font you wish.

- Text that is in orange is for your information only. Text to go on the design is black. Some instructions are in the HPID. Please be creative!

-The design needs to be modern and exciting - colours are to be the green of the logo, and white ...and then choose dark green, or dark grey or black.

Logo - attached (it's not great quality but don't worry, we'll replace it later)

- I've provided the images for the galleries - they are labelled and will match the name in the HPID. Please use the supplied images!

- Examples of some websites that have great design... don't copy them please but they are similar in look to what we are after....
www.qmbbuildworks.co.nz
http://www.rim-safeguard.co.nz/
http://www.lumenhomes.wb.gs/

Important: Width of content will be 1280 pixels when implemented as a web page but the winning design will need to supplied be on a 2000 pixel wide background so nav bars and background can extend outside the 1280 width.
Header height (without nav bar) 150-160 pixels.

We don't comment on individual designs but will choose a winning design promptly.

Industry/Entity Type

Business

Number of Pages Required

1 page

Font styles to use
Sans Serif

Requirements
Must have
• clean, modern, well-spaced design

```html
<!DOCTYPE html>
<html lang="en">
<head>
<meta charset="utf-8">
<title>Turf Tidings – Lawn Specialists</title>
<link href="https://fonts.googleapis.com/css2?family=Open+Sans:wght@300;400;600;700&display=swap" rel="stylesheet">
<style>
:root{
  --green:#6a9f0a;
  --green-dark:#4e7c05;
  --green-light:#9cc93a;
  --text:#555;
  --heading:#333;
  --grey-bg:#eeeeee;
  --line:#d6d6d6;
}
*{box-sizing:border-box;margin:0;padding:0}
html,body{width:1200px;height:2941px;overflow:hidden;background:#fff}
body{font-family:"Open Sans",Arial,sans-serif;color:var(--text);position:relative}
.abs{position:absolute}
/* header */
.header{left:0;top:0;width:1200px;height:114px;background:#fff}
.brand{left:126px;top:22px;display:flex;align-items:center;gap:12px}
.brand-mark{width:34px;height:34px;background:var(--green)}
.brand-name{font-size:30px;font-weight:700;color:var(--green)}
.header-info{right:98px;top:20px;text-align:right;font-size:10px;line-height:17px;color:#666}
.header-info .tag{font-size:14px;font-weight:700;color:var(--green);letter-spacing:.5px;margin-bottom:4px}
.header-info .phone{font-size:16px;font-weight:700;color:var(--green);margin-top:4px}
/* nav */
.nav{left:0;top:114px;width:1200px;height:39px;background:linear-gradient(#8bbf24,#5f9608);display:flex;padding-left:102px}
.nav a{color:#fff;font-size:12px;text-decoration:none;line-height:39px;padding:0 22px}
.nav a.active{background:rgba(0,0,0,.12)}
/* hero */
.hero{left:0;top:153px;width:1200px;height:431px;background:radial-gradient(ellipse at 50% 20%,#d5ee8a,#9ccc33 55%,#6fa813)}
.hero-grass{left:0;top:520px;width:1200px;height:64px;background:linear-gradient(#a9d83f,#5e9a0c)}
.slider{left:102px;top:192px;width:998px;height:322px;background:#fff;padding:8px;display:flex;gap:8px}
.slide{flex:1;position:relative;height:306px}
.slide .photo{position:absolute;inset:0}
.slide .cap{position:absolute;left:0;right:0;bottom:0;height:46px;background:rgba(95,150,10,.92);color:#fff;font-weight:700;font-size:19px;line-height:46px;padding-left:22px}
.arrow{top:340px;width:32px;height:32px;border-radius:50%;background:#333;display:flex;align-items:center;justify-content:center}
/* intro */
.intro{left:137px;top:645px;width:926px;text-align:center}
.intro h1{font-size:21px;font-weight:700;color:var(--green);letter-spacing:.5px}
.intro h2{font-size:20px;font-weight:400;color:#555;margin-top:6px}
.intro p{font-size:11px;line-height:22px;margin-top:16px}
/* service cards */
.card-img{width:500px;height:253px}
.card-title{font-size:14px;font-weight:700;color:var(--green)}
.card-text{font-size:11px;line-height:20px;width:490px;margin-top:8px}
.btn{display:inline-block;background:var(--green);color:#fff;font-size:11px;text-transform:uppercase;text-align:center;line-height:41px;border-bottom:2px solid var(--green-dark);text-decoration:none}
/* video */
.video-title{left:100px;top:1778px;width:440px;font-size:13px;font-weight:700;color:var(--green);line-height:24px;text-transform:uppercase}
.video{left:100px;top:1848px;width:455px;height:285px}
.about{left:608px;top:1775px;width:494px}
.about h3{font-size:38px;font-weight:300;color:#333}
.about p{font-size:11px;line-height:22px;margin-top:20px}
/* testimonial */
.testimonial{left:100px;top:2191px;width:1002px;height:196px;background:var(--grey-bg);border:2px solid var(--line)}
.quote{left:150px;top:2222px;width:480px}
.quote h4{font-size:13px;font-weight:700;color:var(--green);line-height:24px;text-transform:uppercase}
.quote p{font-size:11px;font-style:italic;line-height:22px;margin-top:12px}
.quote .by{text-align:right;margin-top:14px;font-size:11px}
.quote .by b{color:var(--green)}
/* footer */
.footer{left:0;top:2442px;width:1200px;height:298px;background:linear-gradient(#e6e6e6,#fafafa)}
.foot-h{font-size:13px;font-weight:700;color:var(--green)}
.foot-links{font-size:11px;line-height:24px;color:#666;list-style:none}
.field{position:absolute;height:36px;border:1px solid #ccc;background:#fff;font-size:11px;color:#999;padding:9px 12px}
.copyright{left:0;top:2740px;width:1200px;height:43px;background:#fff;text-align:center;font-size:11px;line-height:43px;color:#777;border-top:1px solid #e4e4e4}
.foot-grass{left:0;top:2783px;width:1200px;height:158px;background:linear-gradient(#fff 0%,#b8dc6a 30%,#6fa615 70%,#4c7e06)}
</style>
</head>
<body>

<header class="abs header">
  <div class="abs brand"><span class="brand-mark"></span><span class="brand-name">Turf Tidings</span></div>
  <div class="abs header-info">
    <div class="tag">LAWN SPECIALISTS</div>
    <div>...from ground preparation to lawn aftercare</div>
    <div>Servicing the Auckland region</div>
    <div class="phone">0800 31 42 60</div>
  </div>
</header>

<nav class="abs nav">
  <a class="active">Home</a><a>About us</a><a>Services</a><a>Lawn care</a><a>Seasonal care</a><a>Hydroseeding</a><a>FAQs</a><a>Before &amp; After Gallery</a><a>Quote / Contact</a>
</nav>

<section class="abs hero"></section>
<div class="abs hero-grass" role="img" aria-label="Row of grass blades along the bottom of the banner"></div>
<div class="abs slider">
  <div class="slide"><div class="photo" role="img" aria-label="Bare soil yard before seeding" style="background:linear-gradient(#8a7a6a,#6e5e50)"></div><div class="cap">BEFORE</div></div>
  <div class="slide"><div class="photo" role="img" aria-label="Same yard with a new green lawn" style="background:linear-gradient(#e8e8e4 0%,#e8e8e4 18%,#5ea32a 30%,#3f8a1a)"></div><div class="cap">AFTER</div></div>
</div>
<div class="abs arrow" style="left:78px"><svg width="10" height="12"><path d="M8 1 2 6l6 5" fill="none" stroke="#fff" stroke-width="2"/></svg></div>
<div class="abs arrow" style="left:1090px"><svg width="10" height="12"><path d="M2 1l6 5-6 5" fill="none" stroke="#fff" stroke-width="2"/></svg></div>

<section class="abs intro">
  <h1>YOU CAN ALWAYS SPOT A TURF TIDINGS LAWN</h1>
  <h2>IT'S THE ONE THAT TURNS YOUR NEIGHBOURS GREEN WITH ENVY</h2>
  <p>If you want a lawn or playing field that looks good throughout the year, talk to us. Turf Tidings are New Zealand's experts in high quality grass seeding and lawn maintenance, creating the lushest lawns you'll ever see. With high-tech equipment, years of experience and expert aftercare, nobody knows grass like Turf Tidings. There are many factors that influence the quality of a lawn, including seasonality, growing conditions, shade, seed types, and time. A one-size-fits-all solution couldn't possibly guarantee a great lawn, so we provide personalised advice, a full range of seeding techniques.</p>
</section>

<div class="abs card-img" style="left:100px;top:868px;background:linear-gradient(#5a6a4a,#3f8f8a 55%,#4fa39c)" role="img" aria-label="Freshly hydroseeded garden area"></div>
<div class="abs card-img" style="left:602px;top:868px;background:radial-gradient(circle at 40% 75%,#c8d8c0,#5f9a2a 40%,#3e7a18)" role="img" aria-label="Sprinkler watering a lawn"></div>
<div class="abs" style="left:100px;top:1138px"><div class="card-title">GRASS SEEDING SERVICES</div><p class="card-text">With a wide range of grass seed applications to choose from, including hydroseeding and instant lawn, there is an option to suit your property and your requirements.</p></div>
<div class="abs" style="left:602px;top:1138px"><div class="card-title">LAWN CARE MAINTENANCE</div><p class="card-text">As well as lawn care services, the team at Turf Tidings provides helpful information for regular upkeep of your residential or commercial lawn.</p></div>
<a class="abs btn" style="left:100px;top:1227px;width:255px">Grass seeding &amp; lawn care FAQs</a>
<a class="abs btn" style="left:602px;top:1227px;width:255px">More about ongoing lawn care</a>

<div class="abs card-img" style="left:100px;top:1300px;background:linear-gradient(#b4b09a 0%,#8a8670 35%,#4e9a22 55%,#3c8418)" role="img" aria-label="Established green lawn beside a tree"></div>
<div class="abs card-img" style="left:602px;top:1300px;background:linear-gradient(90deg,#4a8f88 0%,#5a9a8e 50%,#5ea028 50%,#3f8a1a)" role="img" aria-label="Side by side before and after lawn photos"></div>
<div class="abs" style="left:100px;top:1570px"><div class="card-title">FAQS ABOUT GRASS SEEDING AND LAWN CARE</div><p class="card-text">For more information, read our frequently asked questions regarding grass seeding and lawn care.</p></div>
<div class="abs" style="left:602px;top:1570px"><div class="card-title">BEFORE AND AFTER LAWN PHOTOS</div><p class="card-text">See what you potential new lawn could look like by viewing a range of before and after lawn seeding photos.</p></div>
<a class="abs btn" style="left:100px;top:1658px;width:255px">Grass seeding &amp; lawn care FAQs</a>
<a class="abs btn" style="left:602px;top:1658px;width:255px">Before and after photos</a>

<div class="abs video-title">Watch the video on how Turf Tidings can transform your empty spaces into beautiful green grass lawns</div>
<div class="abs video" role="img" aria-label="Video still of a green lawn in front of a house" style="background:linear-gradient(#7a9a6a,#4f8a2a 50%,#3e7a1c)"></div>
<section class="abs about">
  <h3>TURF TIDINGS...</h3>
  <p>For all things grass, you need the best! Turf Tidings are skilled specialists when it comes to creating the perfect lawn for your property.</p>
  <p>From pre-seeding preparation to a full range of grass seeding services and lawn after care options, you'll enjoy a healthy green lawn for many years.</p>
  <p>Selling your property? Turf Tidings will add the wow factor to the outdoor areas of your home with a lush green lawn.</p>
</section>
<a class="abs btn" style="left:608px;top:2066px;width:145px">Find out more</a>

<div class="abs testimonial"></div>
<div class="abs quote">
  <h4>I would recommend Turf Tidings to anyone who wants an amazing lawn</h4>
  <p>Testimonial here about how great Turf Tidings were to deal with and how they are so happy with the lawn and the after care services etc etc.</p>
  <div class="by"><b>- Dan Harlow</b> - Homeowner, Albany</div>
</div>
<div class="abs" style="left:682px;top:2201px;width:410px;height:172px;background:linear-gradient(#5e8a3a,#6cae2a 50%,#4e9a1a)" role="img" aria-label="Lawn mower cutting grass"></div>

<footer class="abs footer">
  <div class="abs foot-h" style="left:100px;top:38px">WELCOME</div>
  <ul class="abs foot-links" style="left:100px;top:62px"><li>Home</li><li>About us</li><li>Services</li><li>Lawn care</li><li>Seasonal care</li><li>Hydroseeding</li></ul>
  <ul class="abs foot-links" style="left:229px;top:62px"><li>FAQs</li><li>Before &amp; After</li><li>Gallery</li><li>Quote / Contact</li></ul>
  <div class="abs" style="left:400px;top:70px;width:170px;height:130px;border-radius:50%;background:var(--green-light)" role="img" aria-label="Horticulture diploma badge"></div>
  <div class="abs foot-h" style="left:651px;top:38px">WELCOME</div>
  <div class="abs" style="left:651px;top:64px;font-size:11px;line-height:20px;color:#666">Get a quote for your new lawn!<br><span style="color:#333;font-weight:600">Fill in the form or phone us on 0800 31 42 60.</span></div>
  <div class="field" style="left:651px;top:117px;width:218px">First name</div>
  <div class="field" style="left:882px;top:117px;width:218px">Last name</div>
  <div class="field" style="left:651px;top:161px;width:218px">Email address</div>
  <div class="field" style="left:882px;top:161px;width:218px">Contact Phone</div>
  <div class="field" style="left:651px;top:205px;width:218px;height:56px">Details</div>
  <a class="abs btn" style="left:882px;top:205px;width:137px">Call me back</a>
</footer>
<div class="abs copyright">Copyright 2015. Turf Tidings Ltd. All rights reserved.</div>
<div class="abs foot-grass" role="img" aria-label="Close-up of grass blades along the page bottom"></div>

</body>
</html>
```